Design Briefpapier
Zielgruppe
Veranstaltungstechnik
Aufgabenstellung
Wir möchten unser Layout (Briefkopf, Header, Footer) neu gestalten lassen. Es existiert bereits ein Logo, das leicht verändert im Header erscheinen soll! WICHTIG: Das Logo soll schwarz hinterlegt werden auf dem Briefpapier, damit das eigentliche Design (orange auf schwarz) auch zur Geltung kommt.
Wir benötigen Briefpapier: Anschreiben, Rechnngsformular in Farbe und in schwarz weiß. Dazu Visitenkarten und ein gleicherscheinenden E-Mail Absender. Das Design sollte so klar wir möglich sein. Der Druck erfolgt auf recyceltem Papier.
Wir benötigen ein Briefpapierbogen sowie ein Visitenkarten Design! Folgende Angaben müssen auf dem Briefpapier sein: - Logo (siehe Anhang) - Anschrift (KT Werkhaus UG (haftungsbeschränkt), Tanne 7, 75318 Wolfach - Wasserzeichen - GF (Jörg Pellinger) - Bankverbindung ( IBAN DE48 2917 5530..
Wir bitten um ein Design für unser Briefpapier. Wir suchen ein hochwertiges Design, das die Werte Vertrauen, Exklusivität und Innovation ausstrahlt. Es soll edel aussehen. Bitte für Telefon, Mail etc. Icons benutzen, damit es für jedermann verständlich ist, unabhängig von der Sprach..
Es sollte clean sein, Farben wie , Weiß, blau, grün, wären von Vorteil. Habe keine besondere Vorstellungen lasse mich gerne überraschen. Siehe .. www.vorkast.de
Bitte inklusive Logo (sollte Recht, Digital/Apps, Medizin illustrieren) - habe das Preisgeld vor diesem Hintergrund erhöht. ------------------------- Die Kanzlei arbeitet an der Schnittstelle von (Medizin-)Recht und Digital. Von daher wären wären Symbole/Gestaltung aus Bereich Medizin, Recht..

```html
<!DOCTYPE html>
<html lang="de">
<head>
<meta charset="utf-8">
<title>Briefpapier hallmannkessler</title>
<link href="https://fonts.googleapis.com/css2?family=Jost:wght@400;500;600&family=Arimo:wght@400;700&family=Nunito:wght@900&display=swap" rel="stylesheet">
<style>
  :root{
    --ink:#262626;
    --paper:#ffffff;
    --orange:#d68a2e;
    --text:#1a1a1a;
    --mark:#ececec;
  }
  *{box-sizing:border-box;margin:0;padding:0}
  html,body{width:1200px;height:960px;overflow:hidden;background:#fff}
  .stage{position:relative;width:1200px;height:960px}
  .label{position:absolute;font-family:"Nunito",sans-serif;font-weight:900;font-size:13px;color:#111}
  .label--letter{left:138px;top:175px}
  .label--second{left:815px;top:33px}
  .label--back{left:815px;top:116px}

  .sheet{position:absolute;background:var(--ink);box-shadow:3px 3px 5px rgba(0,0,0,.35)}
  .sheet--back{left:642px;top:139px;width:504px;height:713px}
  .sheet--second{left:299px;top:30px;width:504px;height:713px;overflow:hidden}
  .sheet--letter{left:55px;top:198px;width:510px;height:725px;transform:rotate(-2.3deg);transform-origin:top left;overflow:hidden}

  .back-disc{position:absolute;left:204px;top:307px;width:97px;height:97px;border-radius:50%;background:var(--orange)}

  .sheet__body{position:absolute;background:var(--paper);overflow:hidden}
  .sheet--second .sheet__body{left:7px;right:7px;top:96px;bottom:50px}
  .sheet--letter .sheet__body{left:12px;right:12px;top:96px;bottom:50px}

  .brand{position:absolute;display:flex;align-items:center;gap:14px;font-family:"Jost",sans-serif;font-weight:500;color:var(--paper);letter-spacing:.5px;line-height:1}
  .brand__dot{width:36px;height:36px;border-radius:50%;background:var(--orange);flex:none}
  .sheet--second .brand{right:32px;top:28px;font-size:38px}
  .sheet--letter .brand{right:40px;top:28px;font-size:38px}

  .watermark{position:absolute;border-radius:50%;background:var(--mark)}
  .sheet--second .watermark{left:325px;top:380px;width:290px;height:290px}
  .sheet--letter .watermark{left:330px;top:390px;width:280px;height:280px}

  .letter{font-family:"Arimo",sans-serif;color:var(--text)}
  .sender-line{position:absolute;left:42px;top:25px;width:200px;height:12px;background:var(--ink);color:var(--paper);font-family:"Jost",sans-serif;font-size:6px;line-height:12px;padding-left:12px}
  .sender-line b{font-weight:600}
  .contact{position:absolute;left:330px;top:12px;font-family:"Jost",sans-serif;font-size:8.5px;line-height:13px;color:#333}
  .contact__company b{font-weight:600}
  .contact__address{margin-top:6px}
  .contact__row{display:flex;align-items:center;gap:4px}
  .contact__row svg{width:9px;height:9px;flex:none}
  .contact__rows{margin-top:4px;margin-left:-11px}
  .contact__mail{color:var(--orange);font-weight:600;margin-top:4px}
  .date{position:absolute;left:335px;top:115px;font-size:8px}
  .subject{position:absolute;left:60px;top:170px;font-size:8px;font-weight:700}
  .body-text{position:absolute;left:62px;top:220px;width:370px;font-size:7.8px;line-height:10px}
  .body-text p{margin-bottom:6px}
  .closing{position:absolute;left:62px;top:400px;font-size:8px}
  .signature{position:absolute;left:62px;top:442px;font-family:"Jost",sans-serif;font-size:9px}
  .signature b{font-weight:600}

  .footer{position:absolute;left:40px;right:20px;bottom:10px;font-family:"Jost",sans-serif;font-size:7px;line-height:11px;color:var(--orange);letter-spacing:.3px}
</style>
</head>
<body>
<main class="stage">
  <span class="label label--second">Briefbogen/Zweitblatt</span>
  <span class="label label--back">Briefbogen/Rückseite</span>
  <span class="label label--letter">Briefbogen</span>

  <section class="sheet sheet--back" aria-label="Briefbogen Rückseite">
    <div class="back-disc"></div>
  </section>

  <section class="sheet sheet--second" aria-label="Briefbogen Zweitblatt">
    <div class="brand"><span class="brand__dot"></span>hallmannkessler</div>
    <div class="sheet__body">
      <div class="watermark"></div>
    </div>
  </section>

  <section class="sheet sheet--letter" aria-label="Briefbogen">
    <div class="brand"><span class="brand__dot"></span>hallmannkessler</div>
    <div class="sheet__body letter">
      <div class="watermark"></div>
      <div class="sender-line">hallmann<b>kessler</b> GmbH &amp; Co. KG | Lindenhofweg 14 | 10965 Berlin</div>
      <address class="contact" style="font-style:normal">
        <div class="contact__company">hallmann<b>kessler</b> GmbH &amp; Co. KG</div>
        <div class="contact__address">Lindenhofweg 14<br>10965 Berlin</div>
        <div class="contact__rows">
          <div class="contact__row"><svg viewBox="0 0 10 10"><path d="M1 4 Q5 1 9 4 L8 5 L6.5 4 L3.5 4 L2 5Z M3 5 H7 L8 8 H2Z" fill="#d68a2e"/></svg>030.412 778 21</div>
          <div class="contact__row"><svg viewBox="0 0 10 10"><rect x="2" y="1" width="6" height="3" fill="none" stroke="#d68a2e"/><rect x="1" y="4" width="8" height="5" fill="none" stroke="#d68a2e"/></svg>030.412 778 22</div>
          <div class="contact__row contact__mail"><svg viewBox="0 0 10 10"><rect x="1" y="2" width="8" height="6" fill="none" stroke="#d68a2e"/><path d="M1 2 L5 6 L9 2" fill="none" stroke="#d68a2e"/></svg>info@hallmann-kessler.de</div>
        </div>
      </address>
      <div class="date">Berlin, den 04.08.2014</div>
      <div class="subject">Layout 1</div>
      <div class="body-text">
        <p>Sehr geehrter Kunde,</p>
        <p>weit hinten, hinter den Wortbergen, fern der Länder Vokalien und Konsonantien leben die Blindtexte. Abgeschieden wohnen sie in Buchstabhausen an der Küste des Semantik, eines großen Sprachozeans.</p>
        <p>Ein kleines Bächlein namens Duden fließt durch ihren Ort und versorgt sie mit den nötigen Regelialien. Es ist ein paradiesmatisches Land, in dem einem gebratene Satzteile in den Mund fliegen.</p>
        <p>Nicht einmal von der allmächtigen Interpunktion werden die Blindtexte beherrscht – ein geradezu unortho-graphisches Leben. Eines Tages aber beschloß eine kleine Zeile Blindtext, ihr Name war Lorem Ipsum, hinaus zu gehen in die weite Grammatik. Der große Oxmox riet ihr davon ab, da es dort wimmele von bösen Kommata, wilden Fragezeichen und hinterhältigen Semikoli, doch das Blindtextchen ließ sich nicht beirren. Es packte seine sieben Versalien, schob sich sein Initial in den Gürtel und machte sich auf den Weg. Als es die ersten Hügel des Kursivgebirges erklommen hatte, warf es einen letzten Blick ...</p>
      </div>
      <div class="closing">Beste Grüße</div>
      <div class="signature">hallmann<b>kessler</b></div>
    </div>
    <div class="footer">Steuer-Nr.: 27/318/66102 | USt-ID Nr: DE318402716 | Bankverbindung: Spreetal Bank | Kontonummer: 0481726300<br>Bankleitzahl: 10050213 | IBAN: DE29100502130481726300 | BIC(SWIFT): SPRT DE BB120</div>
  </section>
</main>
</body>
</html>
```